依頼概要
・概要
美容専門学校のオープンキャンパスの際に配布するステッカーのデザイン(5つ)を複数お願いします。
・詳細
2つのデザインを男子高校生向け、2つのデザインを女子高校生向けのデザインを想定しています。もう1つは、「MAPLECREST ORBIT」の文字の文字ステッカーを製作いただければと思います。
男子高校生向けのデザインに関しては、男らしい感じがいいです。クールな感じがいいかと思います。
女子高校生向けのデザインに関しては、可愛らしい感じがいいです。美容っぽいポップさを出して欲しいです。
丸型の枠や四角の枠など形は自由で大丈夫ですが、全てのデザインに「MAPLECREST ORBIT BEAUTY COLLEGE」の文字を入れていただければと思います。
・データ形式
PNGとAIデータでいただければと思います。
■ 選んだ理由

シンプルな中にも印象に残りやすいデザインでした。販促物ですので、実際に貼って使っていただくことが大変重要ですので、その点においても使いやすいデザインでした。また、非常に多くのデザイン案をご提示いただき、イメージに近いものを多く仕上げていただきました。
ご提案ありがとうございました!

■ 提案者全員のお礼・コメント

タイトなスケジュールでしたが、様々なご提案をいただきありがとうございました。
ターゲット等をしっかりと考慮したバリエーション豊かな作品を多数作成いただき大変嬉しく思います。
残念ながら皆様を選定させていただくことは出来ませんが、ご協力いただいたこと感謝申し上げます。
またご依頼させていただくこともあるかと思いますので、どうぞよろしくお願いいたします。

```html
<!DOCTYPE html>
<html lang="en">
<head>
<meta charset="utf-8">
<title>Maplecrest Orbit Beauty College — Stickers</title>
<link rel="stylesheet" href="https://fonts.googleapis.com/css2?family=Permanent+Marker&family=Montserrat:wght@700&display=swap">
<style>
  :root {
    --page: #ffffff;
    --magenta: #e0157f;
    --blush: #fbe4ee;
    --edge: #d9d9d9;
    --photo-dark: #2f2424;
    --photo-skin: #e6b898;
    --photo-warm: #c4462e;
  }
  html, body {
    margin: 0;
    padding: 0;
    width: 813px;
    height: 1200px;
    overflow: hidden;
    background: var(--page);
  }
  .sheet { display: block; width: 813px; height: 1200px; }
  .sticker-fill { fill: var(--blush); }
  .sticker-edge { fill: none; stroke: var(--edge); stroke-width: 2; }
  .wordmark-script {
    font-family: "Permanent Marker", cursive;
    font-size: 46px;
    fill: var(--magenta);
  }
  .wordmark-sans {
    font-family: "Montserrat", sans-serif;
    font-weight: 700;
    font-size: 46px;
    fill: var(--magenta);
  }
</style>
</head>
<body>
<svg class="sheet" viewBox="0 0 813 1200" xmlns="http://www.w3.org/2000/svg">
  <defs>
    <linearGradient id="portrait-tone" x1="0" y1="0" x2="0" y2="1">
      <stop offset="0" stop-color="var(--photo-dark)"/>
      <stop offset="0.35" stop-color="var(--photo-dark)"/>
      <stop offset="0.5" stop-color="var(--photo-skin)"/>
      <stop offset="0.72" stop-color="var(--photo-dark)"/>
      <stop offset="1" stop-color="var(--photo-warm)"/>
    </linearGradient>
    <clipPath id="clip-top"><circle cx="406" cy="339" r="262"/></clipPath>
    <clipPath id="clip-bottom"><circle cx="406" cy="875" r="262"/></clipPath>
  </defs>

  <g class="sticker sticker--script">
    <circle class="sticker-fill" cx="406" cy="339" r="262" role="img" aria-label="Pale pink diagonal candy-stripe background"/>
    <g clip-path="url(#clip-top)">
      <rect x="505" y="165" width="170" height="440" rx="70" fill="url(#portrait-tone)" role="img" aria-label="Portrait photo of a smiling student with short dark hair in a colourful plaid jacket"/>
    </g>
    <circle class="sticker-edge" cx="406" cy="339" r="262"/>
    <g transform="rotate(-6 320 320)">
      <text class="wordmark-script" x="212" y="228" textLength="270" lengthAdjust="spacingAndGlyphs">MAPLECREST</text>
      <text class="wordmark-script" x="218" y="298">ORBIT</text>
      <text class="wordmark-script" x="226" y="368">BEAUTY</text>
      <text class="wordmark-script" x="236" y="438">COLLEGE</text>
    </g>
  </g>

  <g class="sticker sticker--sans">
    <circle class="sticker-fill" cx="406" cy="875" r="262" role="img" aria-label="Pale pink diagonal candy-stripe background"/>
    <g clip-path="url(#clip-bottom)">
      <rect x="505" y="690" width="170" height="450" rx="70" fill="url(#portrait-tone)" role="img" aria-label="Portrait photo of a smiling student with short dark hair in a colourful plaid jacket"/>
    </g>
    <circle class="sticker-edge" cx="406" cy="875" r="262"/>
    <text class="wordmark-sans" x="192" y="762" textLength="296" lengthAdjust="spacingAndGlyphs">MAPLECREST</text>
    <text class="wordmark-sans" x="192" y="832">ORBIT</text>
    <text class="wordmark-sans" x="192" y="902">BEAUTY</text>
    <text class="wordmark-sans" x="192" y="972">COLLEGE</text>
  </g>
</svg>
</body>
</html>
```